Flyer design for the Harvest Lantern Summit 2019 (HALSUM)

Design a flyer for our annual conference with basic information about the conference: conference logo and year, Conference name: Harvest Lantern Summit Location: Talbot Community Center (Downtown Portland)482 Wexley Street, Portland, ME 04109, Date: August 8th, 9th, 10th and 11th, 2019Start time 7:00PMI would like the following three words added to the flyer. These words describe the vision of the conference: Prophetic, Fire, Overflow,

Contact info:
Website: www.vostel.org
Phone: 207 555 3184
Email: contact@meadowcrest.org

Target Market(s)

Young adults living in the United States

Industry/Entity Type

Religious

Font styles to use
Sans Serif

Colors

Designer to choose colors to be used in the design.

Requirements
Must have
• HALSUM must logo standout, the reader should be able to take a quick look and find key info,
Should not have
• Cross image, church image

```html
<!DOCTYPE html>
<html lang="en">
<head>
<meta charset="utf-8">
<title>Harvest Lantern Summit 2019</title>
<link href="https://fonts.googleapis.com/css2?family=Open+Sans:wght@400;600;700&display=swap" rel="stylesheet">
<style>
  :root {
    --navy: #2c4558;
    --ink: #2b3b47;
    --title: #3d5566;
    --yellow: #f8c12c;
    --yellow-soft: rgba(246, 196, 30, 0.78);
    --white: #ffffff;
    --address: #e3e9ed;
    --brand: #2f6fd0;
  }
  html, body {
    margin: 0;
    padding: 0;
    overflow: hidden;
    background: var(--white);
  }
  .flyer {
    position: relative;
    width: 857px;
    height: 1200px;
    overflow: hidden;
    font-family: "Open Sans", Arial, sans-serif;
    background: var(--white);
  }
  .flyer-shapes {
    position: absolute;
    inset: 0;
  }
  .summit-title {
    position: absolute;
    left: 89px;
    top: 432px;
    margin: 0;
    font-size: 35px;
    line-height: 49px;
    font-weight: 400;
    color: var(--title);
  }
  .vision-word {
    position: absolute;
    left: 89px;
    width: 256px;
    text-align: center;
    font-size: 33px;
    color: var(--ink);
    transform: rotate(18deg);
    transform-origin: center;
  }
  .vision-word--prophetic { top: 658px; }
  .vision-word--fire { top: 755px; }
  .vision-word--overflow { top: 852px; }
  .brand-mark {
    position: absolute;
    left: 97px;
    top: 978px;
    width: 210px;
    text-align: center;
    color: var(--brand);
    font-weight: 700;
  }
  .brand-name {
    display: block;
    font-size: 44px;
    line-height: 50px;
    letter-spacing: 1px;
  }
  .brand-year {
    display: block;
    font-size: 18px;
    letter-spacing: 6px;
    line-height: 22px;
  }
  .info-block {
    position: absolute;
    left: 511px;
    color: var(--white);
  }
  .info-block--location { top: 598px; }
  .info-block--date { top: 840px; }
  .info-heading {
    margin: 0 0 8px;
    font-size: 24px;
    font-weight: 400;
    letter-spacing: 0.5px;
  }
  .info-text {
    margin: 0;
    font-size: 20px;
    line-height: 29px;
    color: var(--address);
  }
  .contact-bar {
    position: absolute;
    left: 0;
    top: 1102px;
    width: 857px;
    height: 98px;
    font-size: 16px;
    color: var(--ink);
  }
  .contact-item {
    position: absolute;
    top: 34px;
    display: flex;
    align-items: center;
    gap: 10px;
  }
  .contact-item--email { left: 86px; }
  .contact-item--phone { left: 404px; }
  .contact-item--web { left: 624px; }
</style>
</head>
<body>
<div class="flyer">
  <svg class="flyer-shapes" width="857" height="1200" viewBox="0 0 857 1200">
    <defs>
      <linearGradient id="photoTone" x1="0" y1="0" x2="1" y2="1">
        <stop offset="0" stop-color="#f1f0ee"/>
        <stop offset="0.55" stop-color="#e4e1dc"/>
        <stop offset="1" stop-color="#b9a894"/>
      </linearGradient>
      <linearGradient id="navyShade" x1="0" y1="0" x2="1" y2="0">
        <stop offset="0" stop-color="#213747"/>
        <stop offset="0.06" stop-color="#2c4558"/>
        <stop offset="1" stop-color="#2c4558"/>
      </linearGradient>
    </defs>
    <rect class="family-photo" x="0" y="0" width="857" height="560" fill="url(#photoTone)" role="img" aria-label="Photo of a family of four sitting against a white brick wall, parents joining raised hands above their two children"/>
    <polygon class="photo-tint" points="0,92 513,251 513,440 0,300" fill="var(--yellow-soft)"/>
    <polygon class="panel-light" points="0,300 430,440 430,1102 0,1102" fill="var(--white)"/>
    <polygon class="panel-accent" points="87,330 430,440 430,466 87,356" fill="var(--yellow)"/>
    <polygon class="panel-dark" points="428,400 857,535 857,1102 428,1102" fill="url(#navyShade)"/>
    <polygon class="vision-tag" points="89,604 345,688 345,764 89,680" fill="var(--yellow)"/>
    <polygon class="vision-tag" points="89,701 345,785 345,861 89,777" fill="var(--yellow)"/>
    <polygon class="vision-tag" points="89,798 345,882 345,958 89,874" fill="var(--yellow)"/>
    <rect class="contact-band" x="0" y="1102" width="857" height="98" fill="var(--yellow)"/>

    <g class="icon-location">
      <circle cx="428" cy="641" r="37" fill="var(--yellow)"/>
      <path d="M428 664 C418 651 413 643 413 635 A15 15 0 0 1 443 635 C443 643 438 651 428 664 Z" fill="none" stroke="var(--white)" stroke-width="2.5"/>
      <circle cx="428" cy="635" r="5.5" fill="none" stroke="var(--white)" stroke-width="2.5"/>
    </g>
    <g class="icon-clock">
      <circle cx="428" cy="882" r="37" fill="var(--yellow)"/>
      <path d="M446 876 A19 19 0 1 1 423 864" fill="none" stroke="var(--white)" stroke-width="2.5" stroke-linecap="round"/>
      <path d="M428 870 L428 883 L437 889" fill="none" stroke="var(--white)" stroke-width="2.5" stroke-linecap="round"/>
    </g>
  </svg>

  <h1 class="summit-title">Harvest<br>Lantern<br>Summit</h1>

  <div class="vision-word vision-word--prophetic">Prophetic</div>
  <div class="vision-word vision-word--fire">Fire</div>
  <div class="vision-word vision-word--overflow">Overflow</div>

  <div class="brand-mark">
    <span class="brand-name">HALSUM</span>
    <span class="brand-year">2019</span>
  </div>

  <section class="info-block info-block--location">
    <h2 class="info-heading">LOCATION</h2>
    <p class="info-text">Talbot Community Center<br>(Downtown Portland)<br>482 Wexley Street,<br>Portland, ME 04109</p>
  </section>

  <section class="info-block info-block--date">
    <h2 class="info-heading">DATE</h2>
    <p class="info-text">August 8th, 9th, 10th and<br>11th, 2019<br>Start time 7:00PM</p>
  </section>

  <footer class="contact-bar">
    <div class="contact-item contact-item--email">
      <svg width="34" height="24" viewBox="0 0 34 24"><rect x="1.5" y="1.5" width="31" height="21" fill="none" stroke="var(--ink)" stroke-width="2.5"/><path d="M2 2 L17 14 L32 2 M2 22 L13 11 M32 22 L21 11" fill="none" stroke="var(--ink)" stroke-width="2.5"/></svg>
      <span>contact@meadowcrest.org</span>
    </div>
    <div class="contact-item contact-item--phone">
      <svg width="24" height="24" viewBox="0 0 24 24"><path d="M6.6 10.8a15.2 15.2 0 0 0 6.6 6.6l2.2-2.2a1 1 0 0 1 1-.25 11.4 11.4 0 0 0 3.6.57 1 1 0 0 1 1 1V20a1 1 0 0 1-1 1A17 17 0 0 1 3 4a1 1 0 0 1 1-1h3.5a1 1 0 0 1 1 1c0 1.25.2 2.45.57 3.57a1 1 0 0 1-.25 1z" fill="var(--ink)"/></svg>
      <span>207 555 3184</span>
    </div>
    <div class="contact-item contact-item--web">
      <svg width="24" height="24" viewBox="0 0 24 24"><circle cx="12" cy="12" r="10" fill="var(--ink)"/><path d="M7 6 C9 8 8 10 10 11 C12 12 11 15 9 17 M15 4 C14 7 16 8 18 8 M16 13 C18 13 19 15 18 18" fill="none" stroke="var(--yellow)" stroke-width="1.8"/></svg>
      <span>www.vostel.org</span>
    </div>
  </footer>
</div>
</body>
</html>
```